Stylish Business Cards Wanted

- DOUBLE SIDED Design Required -

High end, edgy cards for a corporate and personal stylist. Must include logo,
Name: Belinda Forsey
Title: Director and Stylist
telephone : +61 8 8217 4592
email: belinda@thegarbledger.example
website: thegarbledger.example
Tag: Corporate Workwear & Uniform Specialist | Personal Stylist
Would like nice icons for telephone, email, website

Target Market(s)

Businesses wanting stylish uniforms, people wanting stylish wardrobes

Industry/Entity Type

Corporate Workwear Stylist

Contact Information for Business Card

I would like black, white and gold foiling incorporated in the design - possibly a touch of the other colours on my branding guide attached Name: Belinda Forsey Title: Director and Stylist telephone : +61 8 8217 4592 email: belinda@thegarbledger.example website: thegarbledger.example Tag: Corporate Workwear & Uniform Specialist | Personal Stylist Would like nice icons for telephone, email, website

Font styles to use
Other font styles liked:
• Raleway

Colors

Designer to choose colors to be used in the design.

Requirements
Must have
• Gold foil accents

```html
<!DOCTYPE html>
<html lang="en">
<head>
<meta charset="utf-8">
<title>The Garb Ledger – Business Cards</title>
<link href="https://fonts.googleapis.com/css2?family=Raleway:wght@400;600;700;900&family=Dancing+Script:wght@500&display=swap" rel="stylesheet">
<style>
  :root{
    --stage:#3b3b3c;
    --ink:#18161a;
    --paper:#fbfbfa;
    --card-black:#141414;
    --gold:#e5b93a;
    --foil:#d9bd74;
  }
  *{margin:0;padding:0;box-sizing:border-box}
  html,body{width:1200px;height:2694px;overflow:hidden;background:var(--stage)}
  body{display:grid;grid-template-rows:repeat(3,898px);font-family:"Raleway",sans-serif}
  .panel{display:flex;align-items:center;justify-content:center}
  .card{width:900px;height:514px;position:relative;overflow:hidden}

  /* front: black foil */
  .card--front{background:var(--card-black)}
  .card--front .brand{position:absolute;left:0;right:0;top:150px;text-align:center;
    font-weight:700;font-size:64px;letter-spacing:2px;color:var(--foil)}
  .card--front .brand-mark{display:block;width:14px;height:14px;background:var(--foil);margin:0 auto 22px}
  .card--front .tagline{position:absolute;left:0;right:0;bottom:70px;text-align:center;
    font-family:"Dancing Script",cursive;font-size:34px;color:var(--foil)}

  /* back: classic */
  .card--classic{background:var(--paper)}
  .card--classic .brand{position:absolute;left:40px;top:210px;width:330px;text-align:center;
    font-weight:700;font-size:44px;color:var(--ink)}
  .card--classic .divider{position:absolute;left:400px;top:120px;width:2px;height:270px;background:var(--gold)}
  .card--classic .details{position:absolute;left:440px;top:165px}
  .name{font-weight:700;font-size:36px;color:var(--ink)}
  .role{font-family:"Dancing Script",cursive;font-size:26px;color:var(--gold);margin:2px 0 18px}
  .contact{list-style:none;font-size:22px;color:var(--ink)}
  .contact li{display:flex;align-items:center;gap:12px;line-height:32px}
  .icon{width:20px;height:20px;flex:none}

  /* back: bold */
  .card--bold{background:var(--paper)}
  .card--bold .brand{position:absolute;left:40px;top:34px;font-weight:700;font-size:26px;color:var(--ink)}
  .card--bold .contact{position:absolute;right:40px;top:100px;font-weight:600;font-size:20px}
  .card--bold .contact li{justify-content:flex-end;line-height:28px}
  .card--bold .role{position:absolute;right:60px;top:200px;margin:0}
  .big-name{position:absolute;right:24px;bottom:-22px;text-align:right;font-weight:900;font-size:140px;
    line-height:0.85;letter-spacing:-5px;color:var(--ink);text-transform:uppercase}
</style>
</head>
<body>

<section class="panel">
  <article class="card card--front">
    <div class="brand"><span class="brand-mark"></span>The Garb Ledger</div>
    <p class="tagline">Corporate Workwear | Uniform Specialist | Personal Stylist</p>
  </article>
</section>

<section class="panel">
  <article class="card card--classic">
    <div class="brand">The Garb Ledger</div>
    <div class="divider"></div>
    <div class="details">
      <h1 class="name">Belinda Forsey</h1>
      <p class="role">Director and Stylist</p>
      <ul class="contact">
        <li><svg class="icon" viewBox="0 0 24 24"><path fill="#e5b93a" d="M6.6 10.8a15 15 0 0 0 6.6 6.6l2.2-2.2a1 1 0 0 1 1-.25 11.4 11.4 0 0 0 3.6.57 1 1 0 0 1 1 1V20a1 1 0 0 1-1 1A17 17 0 0 1 3 4a1 1 0 0 1 1-1h3.5a1 1 0 0 1 1 1c0 1.25.2 2.45.57 3.57a1 1 0 0 1-.25 1z"/></svg>+61 8 8217 4592</li>
        <li><svg class="icon" viewBox="0 0 24 24"><path fill="#e5b93a" d="M2 5h20v14H2z"/><path fill="none" stroke="#fff" stroke-width="1.6" d="M2 5l10 8 10-8"/></svg>belinda@thegarbledger.example</li>
        <li><svg class="icon" viewBox="0 0 24 24"><g fill="none" stroke="#e5b93a" stroke-width="2"><circle cx="12" cy="12" r="9"/><ellipse cx="12" cy="12" rx="4" ry="9"/><path d="M3 12h18M5 7h14M5 17h14"/></g></svg>thegarbledger.example</li>
      </ul>
    </div>
  </article>
</section>

<section class="panel">
  <article class="card card--bold">
    <div class="brand">The Garb Ledger</div>
    <ul class="contact">
      <li>belinda@thegarbledger.example<svg class="icon" viewBox="0 0 24 24"><path fill="#e5b93a" d="M2 5h20v14H2z"/><path fill="none" stroke="#fff" stroke-width="1.6" d="M2 5l10 8 10-8"/></svg></li>
      <li>+61 8 8217 4592<svg class="icon" viewBox="0 0 24 24"><path fill="#e5b93a" d="M6.6 10.8a15 15 0 0 0 6.6 6.6l2.2-2.2a1 1 0 0 1 1-.25 11.4 11.4 0 0 0 3.6.57 1 1 0 0 1 1 1V20a1 1 0 0 1-1 1A17 17 0 0 1 3 4a1 1 0 0 1 1-1h3.5a1 1 0 0 1 1 1c0 1.25.2 2.45.57 3.57a1 1 0 0 1-.25 1z"/></svg></li>
      <li>thegarbledger.example<svg class="icon" viewBox="0 0 24 24"><g fill="none" stroke="#e5b93a" stroke-width="2"><circle cx="12" cy="12" r="9"/><ellipse cx="12" cy="12" rx="4" ry="9"/><path d="M3 12h18M5 7h14M5 17h14"/></g></svg></li>
    </ul>
    <p class="role">director and stylist</p>
    <h1 class="big-name">Belinda<br>Forsey</h1>
  </article>
</section>

</body>
</html>
```